Brindle Forge mens beard oil and balm needs label design.

Brindle Forge is a new Irish start up business that produces gentlemens grooming products. Our first two products will be beard oil and beard balm and we need label designs for both, there will be 3 beard oil products and 3 beard balm products, so label must be editable for ingrediants and product name.
We want the label to include a vintage/oldschool vibe with celtic influences that will appeal to both the older and younger gentleman.

Our bottles are 50ml blue circular glass bottles, dimensions are ht 92.2mm and diam of 37.22mm

Our tins are round aluminium screw on tins, dimensions are 70mm diam and 25mm ht.

label must have Made in Ireland.
Brindle Forge must be prominent in labels.

winning designer will also get to design future products and other designs eg,stickers t shirt promotional material etc etc.

Ingrediants list can be provided when required.
Pictures of bottle and tin are attached.
Any questions feel free to ask.

Looking forward to seeing the designs.

Thanks
Brindle Forge

Beard Oil ingrediants. Harrowmere Ingrediants- Peach Kernel(prunus persica), Grapeseed(vitis vinifera), Sweet almond(prunus dulcis), Golden Jojoba(simmondsia sinensis), Vitamin E. Essential oils- Grapefruit(citrus paradisi), Peppermint(mentha piperita) eucalyptus(eucalyptus globulas), Lime,cold pressed(citrus aurantifolia) Stonebrand - Peach Kernel(prunus persica), Grapeseed(vitis vinifera), Sweet almond(prunus dulcis), Golden Jojoba(simmondsia sinensis), Vitamin E. Essential oils- sandalwood(amyris balsanifera), cedarwood(cedrus atlantica), Pine(pinus sylvestris) Marshlord- Peach Kernel(prunus persica), Grapeseed(vitis vinifera), Sweet almond(prunus dulcis), Golden Jojoba(simmondsia sinensis), Vitamin E. Essential oils- ho leaf(cinnamomum camphora), Bay,west Indian(pimenta racemosa), Cinnamon leaf(cinnamomum zeylanium), Clove bud( eugenia caryophyllus) ps. ingrediants on balms(Tins) will follow. As for now use same ingrediants as above with inclusion of Shea butter, cocoa butter, natural beeswax Balms tins will keep the same pruducts names as beard oils(bottles) eg Harrowmere beard oil and Harrowmere beard balm. Thanks

Target Market(s)

Any man with a beard or mustache 18-80

Industry/Entity Type

Business

Requirements
Must have
• Made in Ireland
Handmade
room for barcode
room for 3 product name variations of both bottle and tin.
eg. Harrowmere, Stonebrand, Tidewall.

Harrowmere ingrediants- Peach Kernel(prunus persica), Grapeseed(vitis vinifera), Sweet almond(prunus dulcis), Golden Jojoba(simmondsia sinensis), Vitamin E.
Essential oils- Grapefruit(citrus paradisi), Peppermint(mentha piperita) eucalyptus(eucalyptus globulas), Lime,cold pressed(citrus aurantifolia)

Essential oil ingrediants which will change from product to product so must be editible from product to product
Nice to have
• Would be nice to see a Brindle design backround or outter edge.

```html
<!DOCTYPE html>
<html lang="en">
<head>
<meta charset="utf-8">
<title>Brindle Forge Beard Oil – Harrowmere Label</title>
<link rel="stylesheet" href="https://fonts.googleapis.com/css2?family=Cinzel:wght@400;500&family=Oswald:wght@600&family=Courier+Prime&family=Abril+Fatface&display=swap">
<style>
  :root {
    --backdrop: #efefef;
    --label-paper: #ffffff;
    --label-edge: #d8d8d8;
    --ink: #111111;
    --ink-soft: #2a2a2a;
    --banner-text: #ffffff;
  }
  * { margin: 0; padding: 0; box-sizing: border-box; }
  html, body {
    width: 1152px;
    height: 1200px;
    overflow: hidden;
    background: var(--backdrop);
  }
  .label {
    position: absolute;
    left: 189px;
    top: 75px;
    width: 774px;
    height: 1050px;
    background: var(--label-paper);
    border: 1px solid var(--label-edge);
    color: var(--ink);
  }
  .brand-mark {
    position: absolute;
    left: 50%;
    top: 155px;
    width: 122px;
    height: 122px;
    margin-left: -61px;
    border: 5px solid var(--ink);
    border-radius: 50%;
  }
  .brand-name {
    position: absolute;
    top: 342px;
    width: 100%;
    text-align: center;
    font-family: "Cinzel", serif;
    font-weight: 400;
    font-size: 52px;
    letter-spacing: 1px;
    line-height: 1;
  }
  .product-type {
    position: absolute;
    top: 458px;
    width: 100%;
    text-align: center;
    font-family: "Cinzel", serif;
    font-weight: 500;
    font-size: 44px;
    line-height: 1;
  }
  .product-banner {
    position: absolute;
    left: 50%;
    top: 510px;
    width: 360px;
    height: 52px;
    margin-left: -180px;
    background: var(--ink);
    color: var(--banner-text);
    font-family: "Oswald", sans-serif;
    font-weight: 600;
    font-size: 34px;
    letter-spacing: 2px;
    line-height: 52px;
    text-align: center;
  }
  .ingredients {
    position: absolute;
    left: 18px;
    right: 18px;
    top: 596px;
    height: 330px;
    border-top: 3px solid var(--ink);
    border-bottom: 3px solid var(--ink);
    display: flex;
  }
  .ingredients-column {
    width: 50%;
    padding: 14px 8px 0 8px;
    font-family: "Courier Prime", monospace;
    font-size: 21px;
    line-height: 33px;
    letter-spacing: -0.5px;
    color: var(--ink-soft);
    white-space: nowrap;
  }
  .ingredients-column.carrier-oils { border-right: 3px solid var(--ink); }
  .ingredients-column span { display: block; }
  .label-footer {
    position: absolute;
    left: 18px;
    right: 18px;
    top: 932px;
    height: 48px;
    border-bottom: 3px solid var(--ink);
  }
  .handmade {
    position: absolute;
    left: 6px;
    top: 2px;
    font-family: "Abril Fatface", serif;
    font-size: 34px;
    line-height: 1;
  }
  .volume {
    position: absolute;
    left: 400px;
    top: 6px;
    font-family: "Courier Prime", monospace;
    font-size: 28px;
    line-height: 1;
  }
  .origin {
    position: absolute;
    top: 996px;
    width: 100%;
    text-align: center;
    font-family: "Courier Prime", monospace;
    font-size: 24px;
    letter-spacing: 2px;
    line-height: 1;
  }
</style>
</head>
<body>
  <main class="label">
    <div class="brand-mark"></div>
    <h1 class="brand-name">BRINDLE FORGE</h1>
    <h2 class="product-type">BEARD OIL</h2>
    <div class="product-banner">HARROWMERE</div>

    <section class="ingredients">
      <div class="ingredients-column carrier-oils">
        <span>INGREDIANTS-</span>
        <span>PEACHKERNEL(PRUNUS</span>
        <span>PERSICA),</span>
        <span>GRAPESEED(VITIS</span>
        <span>VINIFERA), SWEET</span>
        <span>ALMOND(PRUNUS</span>
        <span>DULCIS), GOLDEN</span>
        <span>JOJOBA(SIMMONDSIA</span>
        <span>SINENSIS), VITAMIN E.</span>
      </div>
      <div class="ingredients-column essential-oils">
        <span>ESSENTIAL OILS-</span>
        <span>GRAPEFRUIT(CITRUS</span>
        <span>PARADISI),</span>
        <span>PEPPERMINT(MENTHA</span>
        <span>PIPERITA)</span>
        <span>EUCALYPTUS(EUCALYPTUS</span>
        <span>GLOBULAS), LIME,COLD</span>
        <span>PRESSED(CITRUS</span>
        <span>AURANTIFOLIA</span>
      </div>
    </section>

    <footer class="label-footer">
      <span class="handmade">HANDMADE</span>
      <span class="volume">50ml</span>
    </footer>
    <p class="origin">MADE IN IRELAND</p>
  </main>
</body>
</html>
```